Business Card Design Project

Hi,
I am after a business card design for a new business. The business is called Quarrel Works and is a stockist of building supplies used for modern cosmetic renovations for houses. (e.g Floorboards, timber decking, modern fittings and fixtures.)
The logo and font faces have been attached.
The logo comes in 2 different color scheme's - 1. Orange on White & 2. Orange on Black. I would like 2 versions of the business card design to reflect these color scheme's.
The designs need to be double sided. The front should contain all the contact information, whilst the back of the card should display the logo and the URL of the webpage - www.quarrelworks-demo.com.au . The logo needs to be displayed creatively on the back of the card.
The business card design needs to reflect the image of modern living, but should also have the wow factor.

```html
<!DOCTYPE html>
<html lang="en">
<head>
<meta charset="utf-8">
<title>Quarrel Works – Business Cards</title>
<link rel="stylesheet" href="https://fonts.googleapis.com/css2?family=Arimo:wght@400;700&family=Michroma&display=swap">
<style>
  :root {
    --stage: #9c9c9c;
    --orange-bright: #ee6a2a;
    --orange-mid: #c9561c;
    --orange-deep: #9a3f10;
    --black: #0b0b0b;
    --white: #ffffff;
    --rule: #5a5a5a;
  }
  * { margin: 0; padding: 0; box-sizing: border-box; }
  html, body { width: 1200px; height: 900px; overflow: hidden; }
  body {
    background: var(--stage);
    font-family: "Arimo", Arial, sans-serif;
    position: relative;
  }
  .card {
    position: absolute;
    left: 268px;
    width: 636px;
    height: 368px;
    overflow: hidden;
  }

  /* Front */
  .card-front {
    top: 50px;
    background: radial-gradient(ellipse 75% 90% at 62% 28%, var(--orange-bright) 0%, var(--orange-mid) 50%, var(--orange-deep) 100%);
  }
  .front-panel {
    position: absolute;
    left: 34px; top: 30px;
    width: 206px; height: 338px;
    background: var(--black);
  }
  .panel-brand {
    position: absolute;
    left: 16px; top: 96px;
    display: flex; align-items: center; gap: 10px;
  }
  .brand-square { background: var(--orange-bright); flex: none; }
  .panel-brand .brand-square { width: 30px; height: 30px; }
  .panel-brand .brand-name {
    color: var(--white); font-size: 19px; font-weight: 400; white-space: nowrap;
  }
  .panel-rule {
    position: absolute; left: 10px; right: 10px; top: 258px;
    height: 1px; background: var(--rule);
  }
  .panel-url {
    position: absolute; left: 0; right: 0; top: 272px;
    text-align: center; color: var(--white); font-size: 14px;
  }
  .faint-square {
    position: absolute; left: 494px; top: 244px;
    width: 72px; height: 72px;
    background: rgba(255,255,255,0.08);
  }
  .holder-name {
    position: absolute; right: 30px; top: 94px;
    font-family: "Michroma", sans-serif;
    font-size: 33px; color: var(--white); letter-spacing: 0.5px;
  }
  .contact {
    position: absolute; right: 30px; top: 200px;
    text-align: right; color: var(--white);
    font-size: 15px; font-weight: 700; line-height: 29px;
  }

  /* Back */
  .card-back {
    top: 466px;
    background: linear-gradient(180deg, var(--orange-mid), var(--orange-deep));
  }
  .back-band {
    position: absolute; left: 0; right: 0; top: 58px; height: 228px;
    background: var(--black);
  }
  .back-band::before, .back-band::after {
    content: ""; position: absolute; left: 0; right: 0; height: 1px; background: var(--rule);
  }
  .back-band::before { top: 6px; }
  .back-band::after { bottom: 6px; }
  .back-brand {
    position: absolute; left: 84px; top: 60px;
    display: flex; align-items: center; gap: 26px;
  }
  .back-brand .brand-square { width: 104px; height: 104px; }
  .back-brand .brand-name {
    color: var(--white); font-size: 52px; font-weight: 400; white-space: nowrap;
  }
  .back-url {
    position: absolute; left: 0; right: 0; top: 318px;
    text-align: center; color: var(--white);
    font-size: 20px; font-weight: 700;
  }
</style>
</head>
<body>
  <section class="card card-front" aria-label="Card front">
    <div class="front-panel">
      <div class="panel-brand">
        <span class="brand-square" aria-hidden="true"></span>
        <span class="brand-name">Quarrel Works</span>
      </div>
      <div class="panel-rule"></div>
      <p class="panel-url">quarrelworks-demo.com.au</p>
    </div>
    <div class="faint-square" aria-hidden="true"></div>
    <h1 class="holder-name">Your Name</h1>
    <address class="contact">
      st. Streat Address<br>
      phone: +61 2 5550 0151<br>
      email: name@quarrelworks-demo.com.au
    </address>
  </section>

  <section class="card card-back" aria-label="Card back">
    <div class="back-band">
      <div class="back-brand">
        <span class="brand-square" aria-hidden="true"></span>
        <span class="brand-name">Quarrel Works</span>
      </div>
    </div>
    <p class="back-url">www.quarrelworks-demo.com.au</p>
  </section>
</body>
</html>
```